Crestline Lending Group Business Cards

We are looking to revamp the current business cards each of our locations uses. We are a lending company that specializes in personal loans, title loans, and tax services. We have locations in New Mexico, Texas, and Oklahoma.

We would like a cleaner, sleeker look while still highlighting what we offer. Title Loans, Personal Loans & Tax Services. We also want to include our referral fee somewhere on the card. We would like to see an English option as well as a Spanish option for the cards.

PLEASE NOTE: Some business cards do not include the employee's name but just the store's location, while others will include both.

These are double-sided business cards, and we would like to see proof if possible. I have included proofs of our current business cards for you to review below, as well as our company logo. Feel free to get creative with the logo, etc! Colors should match the logo; however, you do not need to use all of our logo colors if you don't want to.

```html
<!DOCTYPE html>
<html lang="en">
<head>
<meta charset="utf-8">
<title>Crestline Lending Group Business Cards</title>
<link rel="stylesheet" href="https://fonts.googleapis.com/css2?family=Poppins:wght@400;500&family=Noto+Serif:wght@700&family=Tinos:wght@400;700&display=swap">
<style>
  :root {
    --backdrop: #ababab;
    --card-white: #ffffff;
    --brand-green: #0f4f2c;
    --brand-green-deep: #0d5030;
    --brand-green-light: #14824b;
    --brand-red: #c21f26;
    --ink: #3a3a3a;
  }
  * { margin: 0; padding: 0; box-sizing: border-box; }
  html, body { width: 1093px; height: 1200px; overflow: hidden; }
  body { background: var(--backdrop); position: relative; font-family: "Poppins", sans-serif; }

  .card {
    position: absolute;
    left: 265px;
    width: 576px;
    height: 356px;
    border-radius: 26px;
    overflow: hidden;
  }
  .card p, .card span { position: absolute; line-height: 1; white-space: nowrap; }

  /* Front */
  .card-front { top: 226px; background: var(--card-white); }
  .holder-name { left: 27px; top: 38px; font-family: "Noto Serif", serif; font-weight: 700; font-size: 25px; color: var(--brand-green); }
  .holder-title { left: 27px; top: 70px; font-size: 16px; color: var(--brand-red); }

  .brand-name { right: 42px; top: 50px; text-align: right; font-size: 30px; font-weight: 500; color: var(--brand-green); line-height: 1.15 !important; }
  .brand-web { right: 42px; top: 144px; font-size: 16px; color: var(--brand-red); }

  .contact-line { left: 52px; font-size: 17.5px; color: var(--ink); }
  .contact-phone { top: 197px; }
  .contact-email { top: 219px; }
  .contact-icon { position: absolute; left: 29px; width: 16px; height: 16px; }
  .icon-phone { top: 199px; }
  .icon-email { top: 222px; }

  .address-line { left: 27px; font-size: 17px; color: var(--ink); }
  .address-1 { top: 264px; }
  .address-2 { top: 285px; }

  .service { right: 54px; font-size: 17px; color: var(--brand-green); }
  .service::after { content: ""; position: absolute; right: -12px; top: 6px; width: 6px; height: 6px; border-radius: 50%; background: var(--brand-red); }
  .service-title { top: 243px; }
  .service-personal { top: 264px; }
  .service-tax { top: 285px; }

  .front-swoop { position: absolute; left: 0; top: 0; width: 576px; height: 356px; }

  /* Back */
  .card-back {
    top: 621px;
    background: linear-gradient(90deg, var(--brand-green-deep) 0%, var(--brand-green-light) 12%, var(--brand-green-deep) 30%, var(--brand-green-deep) 100%);
    font-family: "Tinos", serif;
    color: var(--card-white);
  }
  .offer-lead { left: 125px; top: 41px; font-size: 57px; }
  .offer-upto { left: 146px; top: 112px; font-size: 74px; }
  .offer-amount { left: 186px; top: 225px; font-size: 98px; font-weight: 700; color: var(--brand-red); }
</style>
</head>
<body>

<section class="card card-front" aria-label="Business card front">
  <p class="holder-name">Jane Doe</p>
  <p class="holder-title">Branch Manager</p>

  <p class="brand-name">Crestline<br>Lending Group</p>
  <p class="brand-web">www.crestlinelending.com</p>

  <svg class="contact-icon icon-phone" viewBox="0 0 24 24" aria-hidden="true">
    <path fill="#0f4f2c" d="M6.6 10.8c1.4 2.8 3.8 5.1 6.6 6.6l2.2-2.2c.3-.3.7-.4 1-.2 1.1.4 2.3.6 3.6.6.6 0 1 .4 1 1V20c0 .6-.4 1-1 1C10.6 21 3 13.4 3 4c0-.6.4-1 1-1h3.5c.6 0 1 .4 1 1 0 1.3.2 2.5.6 3.6.1.3 0 .7-.2 1z"/>
    <path fill="none" stroke="#0f4f2c" stroke-width="1.6" d="M14 3a7 7 0 0 1 7 7M14 6.5a3.5 3.5 0 0 1 3.5 3.5"/>
  </svg>
  <p class="contact-line contact-phone">(505) 555-0148</p>

  <svg class="contact-icon icon-email" viewBox="0 0 24 18" aria-hidden="true">
    <rect x="1" y="1" width="22" height="16" fill="#0f4f2c"/>
    <path d="M1 1l11 9 11-9M1 17l8-7M23 17l-8-7" fill="none" stroke="#ffffff" stroke-width="1.5"/>
  </svg>
  <p class="contact-line contact-email">jdoe@crestlinelending.com</p>

  <p class="address-line address-1">418 Mesa Avenue, Suite C</p>
  <p class="address-line address-2">Fairview, Texas 75069</p>

  <p class="service service-title">Title Loans</p>
  <p class="service service-personal">Personal Loans</p>
  <p class="service service-tax">Tax Services</p>

  <svg class="front-swoop" viewBox="0 0 576 356" aria-hidden="true">
    <path d="M57 356 Q 300 270 567 345 L 576 356 Z" fill="#c21f26"/>
    <path d="M72 356 Q 300 288 562 350" fill="none" stroke="#ffffff" stroke-width="2.5"/>
  </svg>
</section>

<section class="card card-back" aria-label="Business card back">
  <p class="offer-lead">Refer a Friend</p>
  <p class="offer-upto">Get Upto</p>
  <p class="offer-amount">$100</p>
</section>

</body>
</html>
```